Brightfold websites redesign

Www.bright-fold.com needs to be redesigned along with updations. The incremental material will be provided for the updations. We are looking for complete redesign of the pages with the new content. The complete write up will be provided soon

Target Market(s)

Global

Coding

Coded - Design and coding required

Number of Pages Required

5+ page

Requirements
Must have
• A clean and slick design for the Consulting.
Should not have
• Too many pictures which reduces the speed of the site

```html
<!DOCTYPE html>
<html lang="en">
<head>
<meta charset="utf-8">
<title>Brightfold — Consultancy</title>
<link rel="stylesheet" href="https://fonts.googleapis.com/css2?family=Lato:wght@400;700;900&display=swap">
<style>
:root{
  --navy:#0c2236;
  --navy-2:#13395c;
  --hero-a:#1d4f78;
  --hero-b:#0f2d4a;
  --accent:#35a2cc;
  --cyan:#2fc6d8;
  --ink:#1d2733;
  --muted:#7b8591;
  --light:#eef1f4;
  --white:#ffffff;
  --blue:#1f77c4;
  --olive:#8fa23a;
  --orange:#f0902a;
  --red:#b61f26;
}
*{box-sizing:border-box;margin:0;padding:0}
html,body{width:1200px;height:3197px;overflow:hidden}
body{font-family:'Lato',sans-serif;color:var(--ink);background:var(--white);position:relative}
.abs{position:absolute}

/* header */
.site-header{position:absolute;top:0;left:0;width:1200px;height:88px;background:var(--white)}
.brand{left:85px;top:24px;display:flex;align-items:center;gap:12px;font-size:30px;font-weight:700;color:var(--navy-2)}
.brand-mark{width:34px;height:34px;border-radius:50%;background:var(--accent)}
.main-nav{right:95px;top:22px;display:flex;gap:8px}
.main-nav a{font-size:14px;font-weight:700;color:var(--ink);text-decoration:none;padding:12px 16px;text-transform:uppercase}
.main-nav a.is-active{background:var(--navy-2);color:var(--white)}

/* hero */
.hero{top:88px;left:0;width:1200px;height:632px;background:radial-gradient(ellipse at 55% 40%,#3d7aa6 0%,var(--hero-a) 40%,var(--hero-b) 100%)}
.hero-title{top:200px;width:100%;text-align:center;font-size:52px;font-weight:400;letter-spacing:4px;color:var(--white)}
.hero-title span{color:var(--accent)}
.hero-lead{top:280px;left:280px;width:640px;text-align:center;font-size:20px;font-weight:700;line-height:36px;color:var(--white)}
.btn{display:inline-block;font-weight:900;font-size:13px;text-transform:uppercase;text-decoration:none;text-align:center}
.hero-btn{top:381px;left:554px;width:149px;height:42px;line-height:42px;background:var(--white);color:var(--ink)}

/* trade map */
.trade{top:720px;left:0;width:1200px;height:940px;background:var(--light)}
.section-title{width:100%;text-align:center;font-size:32px;font-weight:400;color:var(--ink)}
.section-sub{width:100%;text-align:center;font-size:15px;font-weight:700;color:var(--muted)}
.trade .section-title{top:54px}
.trade .section-sub{top:100px}
.world-map{top:132px;left:75px;width:990px;height:565px;border-radius:40px;background:radial-gradient(ellipse at 50% 50%,#4a8fd0 0%,#2a77bf 45%,rgba(238,241,244,0) 75%)}
.ranges{top:700px;left:0;width:1200px;height:190px}
.range{position:absolute;top:0;width:188px;height:188px}
.range text{font-family:'Lato',sans-serif;font-size:17px;font-weight:700;fill:var(--white)}

/* founder */
.founder{top:1660px;left:0;width:1200px;height:420px;background:linear-gradient(180deg,#1c3a56,#0f2740)}
.founder-photo{top:83px;left:85px;width:503px;height:286px;border:8px solid var(--white);background:linear-gradient(135deg,#6a2a2e,#3a1a22 55%,#1c1420)}
.founder-name{top:106px;left:614px;font-size:32px;font-weight:400;color:var(--white)}
.founder-bio{top:160px;left:614px;width:500px;font-size:13px;line-height:25px;color:#d8e0e8}
.founder-btn{top:298px;left:614px;width:147px;height:41px;line-height:41px;background:var(--white);color:var(--ink)}

/* case studies */
.cases{top:2080px;left:0;width:1200px;height:592px;background:var(--white)}
.cases .section-title{top:46px}
.cases .section-sub{top:94px;font-size:14px}
.case-card{position:absolute;top:172px;width:239px;height:297px;border:1px solid #e1e5ea;background:var(--white)}
.case-media{height:209px}
.case-label{height:88px;display:flex;align-items:center;justify-content:center;text-align:center;padding:0 18px;font-size:13px;font-weight:700;line-height:20px;color:var(--ink)}
.case-card.is-active .case-label{background:var(--navy);color:var(--white)}
.cases-btn{top:496px;left:526px;width:147px;height:43px;line-height:43px;background:var(--accent);color:var(--white)}

/* news + message */
.bottom{top:2672px;left:0;width:1200px;height:452px;background:var(--navy)}
.block-title{top:60px;font-size:30px;font-weight:700;color:var(--white)}
.news-item{position:absolute;left:85px;width:502px;height:105px;border-bottom:1px solid #3a5068}
.news-date{position:absolute;left:0;top:0;width:90px}
.news-day{height:77px;line-height:77px;text-align:center;font-size:40px;font-weight:900;color:var(--white);background:var(--cyan)}
.news-item.muted .news-day{background:#e9ecef;color:var(--ink)}
.news-month{height:24px;line-height:24px;text-align:center;font-size:13px;color:var(--white);background:#3d5064}
.news-body{position:absolute;left:106px;top:0;width:396px}
.news-title{font-size:16px;font-weight:700;color:var(--white)}
.news-item:first-child .news-title{color:var(--cyan)}
.news-text{margin-top:8px;font-size:12px;line-height:20px;color:#c9d3dd}
.news-more{margin-top:10px;font-size:11px;color:#8d9cab}
.field{position:absolute;left:612px;width:502px;background:var(--white);font-size:12px;color:#a0a8b0;padding:11px 14px}
.submit{top:333px;left:612px;width:502px;height:43px;line-height:43px;background:var(--accent);color:var(--white)}

/* footer */
.site-footer{top:3124px;left:0;width:1200px;height:73px;background:var(--navy-2);color:#b9c6d3;font-size:12px}
.copyright{left:85px;top:28px}
.footer-nav{right:85px;top:28px;display:flex;gap:34px}
.footer-nav a{color:#b9c6d3;text-decoration:none}
</style>
</head>
<body>

<header class="site-header">
  <div class="brand abs"><span class="brand-mark"></span>Brightfold</div>
  <nav class="main-nav abs">
    <a class="is-active" href="#">Home</a><a href="#">Founder</a><a href="#">Consultancy</a><a href="#">System</a><a href="#">Case Studies</a><a href="#">Contact</a>
  </nav>
</header>

<section class="hero abs" role="img" aria-label="Business professional touching a digital interface of world map and network graphics">
  <h1 class="hero-title abs">About <span>Brightfold</span></h1>
  <p class="hero-lead abs">Developing technology platform for better distribution, disintermediation, efficient process flow and cost effective delivery of solutions.</p>
  <a class="btn hero-btn abs" href="#">Know More</a>
</section>

<section class="trade abs">
  <h2 class="section-title abs">World Merchandising Trade 2012 ( USD Billion)</h2>
  <p class="section-sub abs">Source: Global Trade Council</p>
  <div class="world-map abs" role="img" aria-label="World map with countries coloured by merchandise trade volume"></div>
  <div class="ranges abs">
    <svg class="range" style="left:145px" viewBox="0 0 188 188"><circle cx="94" cy="94" r="90" fill="#2c3e55"/><path d="M94 4 A90 90 0 1 0 160 33 L94 94Z" fill="var(--blue)"/><circle cx="94" cy="94" r="78" fill="var(--white)"/><circle cx="94" cy="94" r="68" fill="var(--blue)"/><text x="94" y="100" text-anchor="middle">0-250</text></svg>
    <svg class="range" style="left:386px" viewBox="0 0 188 188"><circle cx="94" cy="94" r="90" fill="#6f7f2a"/><path d="M94 4 A90 90 0 1 0 170 46 L94 94Z" fill="var(--olive)"/><circle cx="94" cy="94" r="78" fill="var(--white)"/><circle cx="94" cy="94" r="68" fill="var(--olive)"/><text x="94" y="100" text-anchor="middle">250-500</text></svg>
    <svg class="range" style="left:626px" viewBox="0 0 188 188"><circle cx="94" cy="94" r="90" fill="#e07a12"/><path d="M94 4 A90 90 0 1 0 176 58 L94 94Z" fill="var(--orange)"/><circle cx="94" cy="94" r="78" fill="var(--white)"/><circle cx="94" cy="94" r="68" fill="var(--orange)"/><text x="94" y="100" text-anchor="middle">500 -1000</text></svg>
    <svg class="range" style="left:867px" viewBox="0 0 188 188"><circle cx="94" cy="94" r="90" fill="var(--red)"/><circle cx="94" cy="94" r="78" fill="var(--white)"/><circle cx="94" cy="94" r="68" fill="var(--red)"/><text x="94" y="100" text-anchor="middle">&gt; 1000</text></svg>
  </div>
</section>

<section class="founder abs">
  <div class="founder-photo abs" role="img" aria-label="Founder speaking at a podium during a conference"></div>
  <h2 class="founder-name abs">Meera Sandhu</h2>
  <p class="founder-bio abs">Ms. Meera Sandhu is the founder director of Brightfold Consultancy Limited (BCL) based at Hong Kong. Meera worked as the Alternate Chief Executive of Northgate Bank, Hong Kong Branch until Jan 2013, heading Corporate Banking business in North Asia and Export Credit Agency business globally. During her tenure, both the businesses increased multifold.</p>
  <a class="btn founder-btn abs" href="#">Know More &nbsp;›</a>
</section>

<section class="cases abs">
  <h2 class="section-title abs">Case Studies</h2>
  <p class="section-sub abs">Some of the deals completed by BCL are summarised below to describe the range of activities undertaken with Corporates</p>
  <article class="case-card" style="left:85px">
    <div class="case-media" role="img" aria-label="Interlocking metal gears" style="background:linear-gradient(135deg,#3a4048,#15191f)"></div>
    <div class="case-label">Export Credit Agency backed long term Project financing</div>
  </article>
  <article class="case-card is-active" style="left:349px">
    <div class="case-media" role="img" aria-label="Magnifying glass over a teal surface" style="background:linear-gradient(135deg,#3dd0e0,#1e9fb8)"></div>
    <div class="case-label">Introducing Regional/Local banks for International Subsidiary Banking</div>
  </article>
  <article class="case-card" style="left:612px">
    <div class="case-media" role="img" aria-label="Hand sketching a flow chart" style="background:linear-gradient(135deg,#f4f4f4,#c9c9cc)"></div>
    <div class="case-label">Structured Financing</div>
  </article>
  <article class="case-card" style="left:876px">
    <div class="case-media" role="img" aria-label="Blue financial chart close-up" style="background:linear-gradient(135deg,#2c7fd8,#0b3e96)"></div>
    <div class="case-label">Bank Lines Business</div>
  </article>
  <a class="btn cases-btn abs" href="#">View All</a>
</section>

<section class="bottom abs">
  <h2 class="block-title abs" style="left:85px">Recent News</h2>
  <div class="abs" style="left:0;top:139px;width:600px">
    <div class="news-item" style="top:0">
      <div class="news-date"><div class="news-day">29</div><div class="news-month">Nov</div></div>
      <div class="news-body"><h3 class="news-title">Your News Title Here</h3><p class="news-text">Lorem ipsum dolor sit amet, consectetur adipiscing elit. Vivamus a aliquet orci. Ut interdum mauris sem, non aliquet felis interdum sit</p><p class="news-more">Read more</p></div>
    </div>
    <div class="news-item muted" style="top:149px">
      <div class="news-date"><div class="news-day">03</div><div class="news-month">Sep</div></div>
      <div class="news-body"><h3 class="news-title">Your News Title Here</h3><p class="news-text">Lorem ipsum dolor sit amet, consectetur adipiscing elit. Vivamus a aliquet orci. Ut interdum mauris sem, non aliquet felis interdum sit</p><p class="news-more">Read more</p></div>
    </div>
  </div>
  <h2 class="block-title abs" style="left:612px">Leave a message</h2>
  <div class="field" style="top:139px;height:36px">Name</div>
  <div class="field" style="top:184px;height:34px">Email</div>
  <div class="field" style="top:226px;height:96px"></div>
  <a class="btn submit abs" href="#">Submit Now</a>
</section>

<footer class="site-footer abs">
  <p class="copyright abs">Copyright 2015 &nbsp;&nbsp; All Rights Reserved</p>
  <nav class="footer-nav abs"><a href="#">Home</a><a href="#">Founder</a><a href="#">Consultancy</a><a href="#">System</a><a href="#">Case studies</a><a href="#">Contact</a></nav>
</footer>

</body>
</html>
```